Craft oriented film company needs a Business Card design

Hi all,
We're a 2-man band film company in New Zealand called Kestrel Pictures. We're good honest blokes, who are very passionate about the craft of film making. I've attached our current logo which has a bit of a crafty/artisan feel that we like. Feel free to use it - or throw the baby out with the bathwater and start again..... you never know, you might inspire a complete brand re-work.

In any case, the vibe we want to give out is that we are solid, dependable and no bullshit - but without compromising creative excellence and being in the now. We like the 'Brooklyn' artisan style of work.

Preferably single sided.

We need the standard stuff:
Name, job title, cellphone, email address and physical address (this can be smaller if you like - street, suburb, city & zip, country [if you want])

Check out our website to learn more about us: kestrelpictures.example

Target Market(s)

Brand marketers and advertising agency creatives looking for video production.

Industry/Entity Type

Baby

Requirements
Should not have
• Nothing flashy or too 'futuristic', we want it to feel grounded and real. A limited colour palette is preferred.
We don't want any film reels or cameras or anything obvious like that.

```html
<!DOCTYPE html>
<html lang="en">
<head>
<meta charset="utf-8">
<title>Kestrel Pictures — Business Card</title>
<link rel="stylesheet" href="https://fonts.googleapis.com/css2?family=Barlow:wght@400;500;600&display=swap">
<style>
  :root {
    --backdrop-light: #f1f1f1;
    --backdrop-dark: #c9c9c9;
    --card: #f4f4f4;
    --ink: #1c1c1c;
    --ink-soft: #3a3a3a;
    --mark: #111111;
    --mark-text: #f4f4f4;
  }
  * { box-sizing: border-box; margin: 0; padding: 0; }
  html, body {
    width: 1200px;
    height: 750px;
    overflow: hidden;
  }
  body {
    background: radial-gradient(ellipse at 50% 30%, var(--backdrop-light) 0%, var(--backdrop-dark) 100%);
    font-family: "Barlow", "Helvetica Neue", Arial, sans-serif;
    color: var(--ink);
    position: relative;
  }
  .business-card {
    position: absolute;
    left: 450px;
    top: 115px;
    width: 300px;
    height: 520px;
    background: var(--card);
    border-radius: 26px;
    box-shadow: 0 10px 24px rgba(0, 0, 0, 0.18);
  }
  .brand-mark {
    position: absolute;
    top: 28px;
    right: 28px;
    width: 104px;
    height: 104px;
    border-radius: 50%;
    background: var(--mark);
    color: var(--mark-text);
    display: flex;
    align-items: center;
    justify-content: center;
    text-align: center;
    font-weight: 600;
    font-size: 15px;
    line-height: 1.05;
    letter-spacing: 0.06em;
    text-transform: uppercase;
  }
  .identity {
    position: absolute;
    left: 40px;
    top: 148px;
  }
  .person-name {
    font-size: 22px;
    font-weight: 500;
    letter-spacing: 0.03em;
    text-transform: uppercase;
  }
  .person-role {
    font-size: 16px;
    font-weight: 400;
    letter-spacing: 0.04em;
    text-transform: uppercase;
    color: var(--ink-soft);
    margin-top: 2px;
  }
  .divider-cross {
    position: absolute;
    left: 42px;
    top: 222px;
    width: 16px;
    height: 16px;
  }
  .contact {
    position: absolute;
    left: 40px;
    top: 262px;
    list-style: none;
    font-size: 14px;
    line-height: 1.45;
    color: var(--ink-soft);
  }
  .contact .address { margin-top: 10px; }
  .rule {
    position: absolute;
    left: 40px;
    top: 404px;
    width: 190px;
    height: 1px;
    background: var(--ink-soft);
  }
  .website {
    position: absolute;
    left: 40px;
    top: 448px;
    font-size: 14px;
    color: var(--ink-soft);
  }
</style>
</head>
<body>
  <article class="business-card">
    <div class="brand-mark">Kestrel<br>Pictures</div>

    <header class="identity">
      <h1 class="person-name">Rowan Hartley</h1>
      <p class="person-role">Producer</p>
    </header>

    <svg class="divider-cross" viewBox="0 0 16 16" aria-hidden="true">
      <line x1="1" y1="1" x2="15" y2="15" stroke="#1c1c1c" stroke-width="1.2"/>
      <line x1="15" y1="1" x2="1" y2="15" stroke="#1c1c1c" stroke-width="1.2"/>
    </svg>

    <ul class="contact">
      <li>+64-21-555-0148</li>
      <li>rowan@kestrelpictures.example</li>
      <li class="address">14 Tamar Lane, Ponsonby</li>
      <li>Auckland 1011</li>
    </ul>

    <div class="rule"></div>

    <p class="website">kestrelpictures.example</p>
  </article>
</body>
</html>
```